We are looking for an effective ad to recruit work from home Loan Officers for our Mortgage Brokerage.
Use the following text...
Earn Mortgage Income in your sleep. Its as easy as 1, 2, 3.....
1) Solicit Potential Applicants (Word of Mouth, Email, Social Media etc.)
2) Take Complete Applications & Submit Them
3) Wait to Get Paid.......(Avg. $2,500 per closing)
"You open the door, we'll finish the deal"
No Experience Necessary
No Goals or Quotas
No Office Hours / Work from Home Office
...and We Fully Reimburse ALL LICENSING FEES!!
Email Resume to mwelby@brightharborloans.example
Bright Harbor Lending Group, Inc.
947 W Caldwell Avenue, #318
Baltimore, MD 21230
NMLS #731860
www.brightharborloans.example
Phone (800) 555-0142
Licensed Mortgage Broker in MD and DC since 1997
Target Market(s)
Professionals looking to earn part time income at Loan Officers, preferably with strong social media following.
Industry/Entity Type
Loan
Look and feel

```html
<!DOCTYPE html>
<html lang="en">
<head>
<meta charset="utf-8">
<title>Loan Officer Recruitment Flyer</title>
<link rel="stylesheet" href="https://fonts.googleapis.com/css2?family=Anton&family=Roboto+Slab:wght@400;600&family=Montserrat:wght@500;600;700&family=Open+Sans:wght@400&display=swap">
<style>
:root{
  --blue:#0e58a6;
  --navy:#163b6e;
  --gold:#a99a33;
  --gold-bright:#cbb321;
  --ink:#2b2b2b;
  --grey-band:#e2e2e2;
  --stage:#333333;
  --paper:#ffffff;
}
*{margin:0;padding:0;box-sizing:border-box}
html,body{width:1200px;height:960px;overflow:hidden;background:var(--stage)}
.flyer{
  position:absolute;left:282px;top:30px;width:700px;height:990px;
  background:var(--paper);transform:scale(0.90909);transform-origin:0 0;overflow:hidden;
  font-family:"Montserrat",sans-serif;color:var(--ink);
}
.rule{position:absolute;left:0;width:700px;height:10px;background:var(--blue)}
.rule-top{top:0}.rule-bottom{bottom:0}
.brand{position:absolute;top:78px;left:0;width:700px;display:flex;justify-content:center;align-items:center;gap:10px}
.brand-dot{width:18px;height:18px;border-radius:50%;background:var(--gold)}
.brand-name{font-family:"Roboto Slab",serif;font-weight:600;font-size:22px;color:var(--navy);white-space:nowrap}
.headline{position:absolute;top:148px;left:0;width:700px;text-align:center;font-family:"Roboto Slab",serif;font-weight:600;font-size:33px;line-height:40px;color:#1a1a1a;white-space:nowrap}
.subhead{position:absolute;top:188px;left:0;width:700px;text-align:center;font-family:"Anton",sans-serif;font-weight:400;font-size:70px;line-height:74px;color:var(--blue);letter-spacing:0.5px;word-spacing:6px;white-space:nowrap;z-index:2}
.photo{position:absolute;left:334px;top:270px;width:366px;height:400px;z-index:0;
  background:radial-gradient(ellipse at 65% 45%,#d9b59a 0%,#e9d6c6 35%,#f6efe8 65%,#ffffff 100%)}
.steps{position:absolute;left:0;top:280px;z-index:1}
.step-num{position:absolute;font-family:"Anton",sans-serif;color:#fff;font-size:74px;line-height:1;z-index:2}
.step-text{position:absolute;color:#fff;font-weight:600;font-size:14px;line-height:17px;white-space:nowrap;z-index:2}
.banner{position:absolute;left:0;top:670px;width:700px;height:38px;background:var(--blue);z-index:2;
  color:#fff;font-family:"Roboto Slab",serif;font-size:26px;text-align:center;line-height:38px;white-space:nowrap}
.perk{position:absolute;top:708px;width:146px;height:82px;border:3px solid var(--gold);border-top:none;border-radius:0 0 10px 10px;
  display:flex;align-items:center;justify-content:center;text-align:center;font-weight:600;font-size:14px;line-height:19px;color:var(--navy)}
.reimburse{position:absolute;top:810px;left:0;width:700px;text-align:center;font-weight:700;font-size:18px;letter-spacing:0.3px;color:#2a2a2a;white-space:nowrap}
.apply{position:absolute;left:0;top:848px;width:314px;height:57px;background:var(--gold);color:#fff;
  font-weight:700;font-size:13.5px;line-height:21px;padding:7px 0 0 20px;white-space:nowrap;overflow:hidden}
.apply-lead{font-size:17px}
.contact{position:absolute;left:314px;top:848px;width:386px;height:57px;background:var(--grey-band);
  font-family:"Open Sans",sans-serif;font-size:10.5px;line-height:15px;color:#333;padding:4px 0 0 12px;white-space:nowrap}
.contact svg{vertical-align:-2px;margin-right:3px}
.social{position:absolute;left:100px;top:915px;width:153px;height:50px;border:2px solid var(--navy);border-radius:3px;
  display:flex;align-items:center;justify-content:center;gap:7px;font-weight:700;font-size:12px;color:var(--navy);white-space:nowrap}
.social-square{width:20px;height:20px;background:var(--navy);flex:none}
.license{position:absolute;left:342px;top:932px;font-family:"Open Sans",sans-serif;font-size:12px;color:#333;white-space:nowrap}
</style>
</head>
<body>
<main class="flyer">
  <div class="rule rule-top"></div>

  <div class="photo" role="img" aria-label="Photo of a smiling woman holding a fan of dollar bills"></div>

  <div class="brand"><span class="brand-dot"></span><span class="brand-name">Bright Harbor Lending Group, Inc.</span></div>

  <h1 class="headline">Earn Mortgage Income in your sleep</h1>
  <h2 class="subhead">ITS AS EASY AS 1 2 3</h2>

  <svg class="steps" width="340" height="390" viewBox="0 280 340 390">
    <path d="M0 288 H313 Q335 288 335 310 V440 L300 460 L265 440 V360 H0 Z" fill="var(--gold-bright)"/>
    <path d="M0 288 H265 V360 H0 Z" fill="var(--gold)"/>
    <path d="M55 435 H335 V510 H85 V580 L50 600 L15 580 V475 Q15 435 55 435 Z" fill="var(--navy)"/>
    <path d="M85 435 H335 V510 H85 Z" fill="var(--blue)"/>
    <path d="M15 580 H275 V655 H50 Q15 655 15 620 Z" fill="var(--gold)"/>
  </svg>
  <div class="step-num" style="left:30px;top:288px">1</div>
  <div class="step-text" style="left:75px;top:290px">Solicit Potential<br>Applicants (Word of<br>Mouth, Email, Social<br>Media etc.)</div>
  <div class="step-num" style="left:224px;top:437px">2</div>
  <div class="step-text" style="left:88px;top:448px;text-align:right;width:128px">Take Complete<br>Applications<br>&amp; Submit Them</div>
  <div class="step-num" style="left:88px;top:582px">3</div>
  <div class="step-text" style="left:140px;top:593px">Wait to Get Paid....<br>(Avg. $2,500<br>per closing)</div>

  <div class="banner">You open the door, we'll finish the deal</div>

  <div class="perk" style="left:62px">No Experience<br>Necessary</div>
  <div class="perk" style="left:270px">No Goals or<br>Quotas</div>
  <div class="perk" style="left:485px">No Office<br>Hours / Work from<br>Home Office</div>

  <p class="reimburse">AND WE FULLY REIMBURSE&nbsp; ALL LICENSING FEES!!</p>

  <div class="apply"><span class="apply-lead">Email Resume to</span><br>mwelby@brightharborloans.example</div>
  <div class="contact">
    <div><svg width="10" height="10" viewBox="0 0 10 10"><circle cx="5" cy="5" r="4.3" fill="none" stroke="var(--blue)" stroke-width="1.2"/><path d="M3.3 3 Q3.5 6 7 6.7" fill="none" stroke="var(--blue)" stroke-width="1.2"/></svg>(800) 555-0142 &nbsp;&nbsp;<svg width="10" height="10" viewBox="0 0 10 10"><circle cx="5" cy="5" r="4.3" fill="none" stroke="var(--blue)" stroke-width="1"/><ellipse cx="5" cy="5" rx="2" ry="4.3" fill="none" stroke="var(--blue)" stroke-width="0.8"/><path d="M0.7 5 H9.3" stroke="var(--blue)" stroke-width="0.8"/></svg>www.brightharborloans.example</div>
    <div><svg width="10" height="10" viewBox="0 0 10 10"><path d="M5 0.5 A3.3 3.3 0 0 1 8.3 3.8 C8.3 6 5 9.5 5 9.5 C5 9.5 1.7 6 1.7 3.8 A3.3 3.3 0 0 1 5 0.5 Z" fill="var(--blue)"/></svg>Bright Harbor Lending Group, Inc.</div>
    <div style="padding-left:13px">947 W Caldwell Avenue, #318, Baltimore, MD 21230, NMLS #731860</div>
  </div>

  <div class="social"><span class="social-square"></span>Like us on Neighborly</div>
  <p class="license">Licensed Mortgage Broker in MD and DC since 1997</p>

  <div class="rule rule-bottom"></div>
</main>
</body>
</html>
```